Antigen Preservation Bureau

The company will provide a contract research services to stabilize various viruses, viral vectors, and vaccines. It may offer some licensing opportunities for stabilizing technologies. Main area of applications are pharmaceutical, therapeutic, and vaccination field. The company aspires to develop room temperature vaccines for global distribution beyond the current cold chain.

Target Market(s)

pharmaceutical, therapeutic and vaccination fields

Coding

Coded - Design and coding required

Number of Pages Required

4 page

Requirements
Must have
• Incorporate a APB logo, attached at the bottom, on the Web page

```html
<!DOCTYPE html>
<html lang="en">
<head>
<meta charset="utf-8">
<title>APB — Antigen Preservation Bureau</title>
<link href="https://fonts.googleapis.com/css2?family=Montserrat:wght@400;500&family=Open+Sans:wght@400&display=swap" rel="stylesheet">
<style>
:root{
  --grad-start:#b474b4;
  --grad-end:#4f6fdb;
  --white:#ffffff;
  --ink:#1b1b1b;
  --body:#2a2a2a;
  --accent:#4360d6;
  --rule:#7a6a78;
  --icon:#4a5bd0;
  --icon-border:#6a7ae0;
}
*{margin:0;padding:0;box-sizing:border-box}
html,body{width:1200px;height:1200px;overflow:hidden;background:var(--white)}
body{position:relative;font-family:"Open Sans",sans-serif;color:var(--body)}
.band{position:absolute;left:0;width:1200px;background:linear-gradient(90deg,var(--grad-start),var(--grad-end))}
.hero{top:0;height:514px}
.facts{top:959px;height:241px}
.nav{position:absolute;top:0;left:0;width:1200px;height:72px}
.brand{position:absolute;left:162px;top:18px;font-family:"Montserrat",sans-serif;font-size:26px;font-weight:400;color:var(--white);letter-spacing:0.5px}
.menu{position:absolute;right:174px;top:28px;display:flex;gap:24px;list-style:none}
.menu li{font-size:12px;color:var(--white);letter-spacing:0.2px}
.hero-copy{position:absolute;top:172px;left:0;width:1200px;text-align:center;color:var(--white)}
.hero-title{font-family:"Montserrat",sans-serif;font-weight:400;font-size:39px;letter-spacing:1px;line-height:1}
.hero-text{width:570px;margin:18px auto 0;font-size:13px;line-height:18px}
.btn{display:inline-block;margin-top:33px;width:120px;height:38px;line-height:36px;border:1px solid var(--white);border-radius:19px;font-size:12px;letter-spacing:0.5px;color:var(--white)}
.dots{position:absolute;top:465px;left:567px;display:flex;gap:8px}
.dots span{width:16px;height:16px;border-radius:50%;background:rgba(255,255,255,.5)}
.dots span.active{background:var(--white)}
.about-title{position:absolute;top:578px;left:0;width:1200px;text-align:center;font-family:"Montserrat",sans-serif;font-weight:400;font-size:26px;color:var(--ink);letter-spacing:0.5px}
.about-title em{font-style:normal;color:var(--accent)}
.rule{position:absolute;top:618px;left:561px;width:78px;height:2px;background:var(--rule)}
.about-text{position:absolute;top:641px;left:0;width:1200px;text-align:center;font-size:12px;color:var(--ink)}
.feature{position:absolute;top:722px;width:200px;margin-left:-100px;text-align:center}
.feature-icon{width:40px;height:40px;margin:0 auto;border:1px solid var(--icon-border);border-radius:5px;display:flex;align-items:center;justify-content:center}
.feature-title{margin-top:21px;font-family:"Montserrat",sans-serif;font-weight:500;font-size:18px;color:var(--ink)}
.feature-text{margin-top:14px;font-size:12px;line-height:18px;color:var(--ink)}
.facts-title{position:absolute;top:1078px;left:0;width:1200px;text-align:center;font-family:"Montserrat",sans-serif;font-weight:400;font-size:24px;color:var(--white);letter-spacing:0.5px}
.fact-icon{position:absolute;top:1176px;width:36px;height:36px;margin-left:-18px}
</style>
</head>
<body>
<div class="band hero" role="img" aria-label="Hero background photo of laboratory vaccine research"></div>
<header class="nav">
  <div class="brand">APB</div>
  <ul class="menu">
    <li>HOME</li><li>ABOUT US</li><li>SERVICES</li><li>PORTFOLIO</li><li>TEAM</li><li>OUR CLIENTS</li><li>CONTACT</li>
  </ul>
</header>
<section class="hero-copy">
  <h1 class="hero-title">WELCOME TO APB</h1>
  <p class="hero-text">Lorem Ipsum is simply dummy text of the printing and typesetting industry. Lorem Ipsum has been the industry's standard dummy text ever</p>
  <span class="btn">CONTACT US</span>
</section>
<div class="dots"><span class="active"></span><span></span><span></span></div>

<h2 class="about-title">ABOUT <em>US</em></h2>
<div class="rule"></div>
<p class="about-text">Lorem Ipsum is simply dummy text of the printing and typesetting industry. Lorem Ipsum has been the industry's standard dummy text ever</p>

<div class="feature" style="left:253px">
  <div class="feature-icon"><svg width="20" height="20" viewBox="0 0 20 20" fill="none" stroke="var(--icon)" stroke-width="1.3"><path d="M11 2l7 7-9 9-7-7 2-7z"/><circle cx="12.5" cy="6" r="1.3"/><path d="M7 10l3 3"/></svg></div>
  <h3 class="feature-title">Clean Code</h3>
  <p class="feature-text">Lorem ipsum dolor sit amet, consect adipis elit minim veniam ettis inkeras.</p>
</div>
<div class="feature" style="left:484px">
  <div class="feature-icon"><svg width="20" height="20" viewBox="0 0 20 20" fill="none" stroke="var(--icon)" stroke-width="1.3"><circle cx="10" cy="10" r="2.6"/><path d="M10 2v2.5M10 15.5V18M2 10h2.5M15.5 10H18M4.3 4.3l1.8 1.8M13.9 13.9l1.8 1.8M4.3 15.7l1.8-1.8M13.9 6.1l1.8-1.8"/><circle cx="10" cy="10" r="5.5"/></svg></div>
  <h3 class="feature-title">Great Features</h3>
  <p class="feature-text">Lorem ipsum dolor sit amet, consect adipis elit minim veniam ettis inkeras.</p>
</div>
<div class="feature" style="left:715px">
  <div class="feature-icon"><svg width="20" height="22" viewBox="0 0 20 22" fill="none" stroke="var(--icon)" stroke-width="1.3"><rect x="4" y="2" width="12" height="18" rx="1.5"/><path d="M9 4.5h2"/><circle cx="10" cy="17" r="0.6" fill="var(--icon)"/></svg></div>
  <h3 class="feature-title">Responsive Design</h3>
  <p class="feature-text">Lorem ipsum dolor sit amet, consect adipis elit minim veniam ettis inkeras.</p>
</div>
<div class="feature" style="left:946px">
  <div class="feature-icon"><svg width="22" height="22" viewBox="0 0 22 22" fill="none" stroke="var(--icon)" stroke-width="1.3"><path d="M3 6h8v13H3z"/><path d="M8 3h7l4 4v11h-8"/><path d="M15 3v4h4"/></svg></div>
  <h3 class="feature-title">Well Documented</h3>
  <p class="feature-text">Lorem ipsum dolor sit amet, consect adipis elit minim veniam ettis inkeras.</p>
</div>

<div class="band facts"></div>
<h2 class="facts-title">SOME FACTS ABOUT US</h2>
<svg class="fact-icon" style="left:253px" viewBox="0 0 36 36" fill="none" stroke="var(--white)" stroke-width="2"><path d="M4 16h6v16H4z"/><path d="M10 17l6-12c3 0 4 2 3 6l-1 4h10c2 0 3 2 2 4l-3 11c-1 2-2 2-4 2H10"/></svg>
<svg class="fact-icon" style="left:484px" viewBox="0 0 36 36" fill="none" stroke="var(--white)" stroke-width="2"><circle cx="18" cy="18" r="15"/></svg>
<svg class="fact-icon" style="left:715px" viewBox="0 0 36 36" fill="none" stroke="var(--white)" stroke-width="2"><path d="M11 2v6M16 2v6M21 2v6"/><path d="M5 12h24v18H5z"/><path d="M29 16h3v8h-3"/></svg>
<svg class="fact-icon" style="left:946px" viewBox="0 0 36 36" fill="none" stroke="var(--white)" stroke-width="2"><path d="M9 4h18v10a9 9 0 0 1-18 0z"/><path d="M9 7H3c0 6 3 9 7 9M27 7h6c0 6-3 9-7 9"/><path d="M18 23v6M12 32h12"/></svg>
</body>
</html>
```